Business Card

We need a business card for a fundraising/sales and marketing company called Kelvora Appeals services. The logo colours are Red Black and white. The final design should communicate professional, reliable yet fun and charity minded
Updates

Sorry for the delay. A decision will be made in the next 48 hours. we are stuck between two designs. Kind Regards, Molly Ravenscroft

Industry/Entity Type

Marketing

```html
<!DOCTYPE html>
<html lang="en">
<head>
<meta charset="utf-8">
<title>Kelvora Appeals services – Business Card</title>
<link rel="stylesheet" href="https://fonts.googleapis.com/css2?family=Arimo:wght@400;700&family=Cinzel:wght@400&display=swap">
<style>
  :root {
    --page-bg: #e9e9ea;
    --card-white: #ffffff;
    --brand-red: #d42228;
    --brand-charcoal: #4a4b4b;
    --text-grey: #555657;
    --divider: #6b6b6b;
  }
  html, body {
    margin: 0;
    padding: 0;
    width: 1200px;
    height: 864px;
    overflow: hidden;
    background: var(--page-bg);
  }
  .business-card {
    position: absolute;
    left: 100px;
    top: 146px;
    width: 1000px;
    height: 571px;
    background: var(--card-white);
    box-shadow: 0 10px 30px rgba(0,0,0,0.12);
    overflow: hidden;
    font-family: "Arimo", Arial, sans-serif;
  }
  .card-bands {
    position: absolute;
    inset: 0;
    width: 100%;
    height: 100%;
  }
  .band-charcoal { fill: var(--brand-charcoal); }
  .band-red { fill: var(--brand-red); }

  .brand {
    position: absolute;
    top: 120px;
    left: 0;
    width: 1000px;
    display: flex;
    justify-content: center;
    align-items: center;
    gap: 14px;
  }
  .brand-dot {
    width: 22px;
    height: 22px;
    border-radius: 50%;
    background: var(--brand-red);
  }
  .brand-name {
    font-size: 40px;
    font-weight: 700;
    color: var(--brand-red);
    letter-spacing: 1px;
  }

  .contact-list {
    position: absolute;
    left: 110px;
    top: 280px;
    margin: 0;
    padding: 0;
    list-style: none;
  }
  .contact-item {
    display: flex;
    align-items: center;
    height: 46px;
    font-size: 27px;
    color: var(--text-grey);
  }
  .contact-icon {
    width: 26px;
    height: 26px;
    margin-right: 34px;
    fill: var(--text-grey);
  }

  .divider {
    position: absolute;
    left: 470px;
    top: 260px;
    width: 2px;
    height: 150px;
    background: var(--divider);
  }

  .holder-name {
    position: absolute;
    left: 540px;
    top: 290px;
    font-family: "Cinzel", "Times New Roman", serif;
    font-size: 34px;
    color: var(--text-grey);
    letter-spacing: 1px;
  }

  .website {
    position: absolute;
    left: 0;
    top: 436px;
    width: 760px;
    text-align: center;
    font-size: 26px;
    color: var(--card-white);
    letter-spacing: 0.5px;
  }
</style>
</head>
<body>
  <div class="business-card">
    <svg class="card-bands" viewBox="0 0 1000 571" preserveAspectRatio="none" aria-hidden="true">
      <path class="band-charcoal" d="M690 420 C820 385 930 290 1000 170 L1000 571 L690 571 Z"/>
      <path class="band-red" d="M0 415 L740 415 C850 395 950 310 1000 225 L1000 500 L0 500 Z"/>
      <path class="band-charcoal" d="M0 495 L1000 475 L1000 571 L0 571 Z"/>
    </svg>

    <div class="brand">
      <span class="brand-dot"></span>
      <span class="brand-name">Kelvora Appeals</span>
    </div>

    <ul class="contact-list">
      <li class="contact-item">
        <svg class="contact-icon" viewBox="0 0 24 24" aria-hidden="true">
          <path d="M12 2C8 2 5 5 5 9c0 5 7 13 7 13s7-8 7-13c0-4-3-7-7-7zm0 9.5A2.5 2.5 0 1 1 12 6.5a2.5 2.5 0 0 1 0 5z"/>
        </svg>
        <span>Your address</span>
      </li>
      <li class="contact-item">
        <svg class="contact-icon" viewBox="0 0 24 24" aria-hidden="true">
          <path d="M6.6 10.8c1.4 2.8 3.8 5.1 6.6 6.6l2.2-2.2c.3-.3.7-.4 1-.2 1.1.4 2.3.6 3.6.6.6 0 1 .4 1 1V20c0 .6-.4 1-1 1C10.6 21 3 13.4 3 4c0-.6.4-1 1-1h3.5c.6 0 1 .4 1 1 0 1.3.2 2.5.6 3.6.1.3 0 .7-.2 1L6.6 10.8z"/>
        </svg>
        <span>000 0000 0000</span>
      </li>
      <li class="contact-item">
        <svg class="contact-icon" viewBox="0 0 24 24" aria-hidden="true">
          <path d="M3 6h18v12H3V6zm2 1.5 7 5.5 7-5.5H5zm14 1.8-7 5.4-7-5.4V16h14V9.3z"/>
        </svg>
        <span>inof@email.com</span>
      </li>
    </ul>

    <div class="divider"></div>

    <div class="holder-name">Your Name</div>

    <div class="website">www.yourwebsite.com</div>
  </div>
</body>
</html>
```